Hi,

I would like to have a invitation made for a party. exactly like the picture in the link below.

http://pinboardia.example/pin/730215948361027459/

However, Please change the colors into fun/ girly feeling. font can be different and size of the card should be the same

Name of the girl: RINA
What: Bachelorette Party
Where:TOLO Boat
Dubai Coral Quay Sailing Club
When:7th of February 2013

No RSVP required. (so no need to put it)

```html
<!DOCTYPE html>
<html lang="en">
<head>
<meta charset="utf-8">
<title>RINA – Bachelorette Party Invitation</title>
<link rel="stylesheet" href="https://fonts.googleapis.com/css2?family=Rye&family=Oswald:wght@200;700&family=Cinzel:wght@400&display=swap">
<style>
  :root {
    --blush: #fff4f7;
    --blush-deep: #fbe1ea;
    --berry: #b3306e;
    --berry-soft: #f6cfdd;
    --hot-pink: #ec4d86;
    --lilac: #a77bd6;
    --aqua: #4cc3d9;
    --fold: #f0b9cc;
    --white: #ffffff;
  }
  html, body {
    margin: 0;
    padding: 0;
    width: 1200px;
    height: 575px;
    overflow: hidden;
    background: var(--blush);
  }
  .invitation {
    position: relative;
    width: 1200px;
    height: 575px;
    background: radial-gradient(ellipse at 50% 45%, var(--blush) 55%, var(--blush-deep) 100%);
  }
  .invitation svg { display: block; }
  .name-title {
    font-family: "Rye", serif;
    fill: var(--berry);
  }
  .tagline {
    font-family: "Oswald", sans-serif;
    font-weight: 200;
    fill: var(--lilac);
  }
  .single-word {
    font-family: "Rye", serif;
  }
  .detail-label {
    font-family: "Oswald", sans-serif;
    font-weight: 700;
    fill: var(--berry);
    text-anchor: middle;
  }
  .detail-value {
    font-family: "Cinzel", serif;
    fill: var(--hot-pink);
    text-anchor: middle;
  }
</style>
</head>
<body>
<main class="invitation">
  <svg width="1200" height="575" viewBox="0 0 1200 575" aria-labelledby="invite-title">
    <title id="invite-title">RINA – last chance to celebrate being single. Bachelorette party, 7th of February 2013, TOLO Boat, Dubai Coral Quay Sailing Club.</title>
    <defs>
      <linearGradient id="fade-pink-aqua" x1="0" y1="0" x2="0" y2="1">
        <stop offset="0" stop-color="var(--hot-pink)"/>
        <stop offset="0.5" stop-color="var(--lilac)"/>
        <stop offset="1" stop-color="var(--aqua)"/>
      </linearGradient>
      <linearGradient id="fade-aqua-pink" x1="0" y1="0" x2="0" y2="1">
        <stop offset="0" stop-color="var(--aqua)"/>
        <stop offset="0.5" stop-color="var(--lilac)"/>
        <stop offset="1" stop-color="var(--hot-pink)"/>
      </linearGradient>
    </defs>

    <g class="panel-folds" stroke="var(--fold)" stroke-width="1">
      <line x1="403" y1="0" x2="403" y2="575"/>
      <line x1="800" y1="0" x2="800" y2="575"/>
    </g>

    <g class="background-flourish" fill="var(--berry-soft)" opacity="0.35">
      <ellipse cx="200" cy="90" rx="130" ry="50" role="img" aria-label="faint decorative scrollwork"/>
      <ellipse cx="600" cy="110" rx="140" ry="55" role="img" aria-label="faint decorative scrollwork"/>
      <ellipse cx="990" cy="300" rx="170" ry="200" role="img" aria-label="faint decorative scrollwork"/>
    </g>

    <rect class="corner-ornament" x="316" y="10" width="78" height="80" rx="6" fill="var(--berry-soft)" role="img" aria-label="corner ornament"/>
    <rect class="corner-ornament" x="18" y="485" width="78" height="80" rx="6" fill="var(--berry-soft)" role="img" aria-label="corner ornament"/>

    <text class="name-title" x="30" y="205" font-size="96" textLength="350" lengthAdjust="spacing">RINA</text>
    <text class="tagline" x="20" y="268" font-size="64" textLength="365" lengthAdjust="spacingAndGlyphs">LAST CHANCE TO</text>
    <text class="tagline" x="420" y="268" font-size="64" textLength="375" lengthAdjust="spacingAndGlyphs">CELEBRATE BEING</text>

    <g class="divider" stroke="var(--berry)" stroke-width="2" fill="var(--hot-pink)">
      <line x1="462" y1="183" x2="745" y2="183"/>
      <circle cx="603" cy="183" r="6" stroke="none"/>
    </g>

    <g class="single-word" font-size="200">
      <text x="35" y="438" fill="var(--berry-soft)" textLength="360" lengthAdjust="spacingAndGlyphs">SIN</text>
      <text x="30" y="432" fill="url(#fade-pink-aqua)" textLength="360" lengthAdjust="spacingAndGlyphs">SIN</text>
      <text x="415" y="438" fill="var(--berry-soft)" textLength="368" lengthAdjust="spacingAndGlyphs">GLE</text>
      <text x="410" y="432" fill="url(#fade-aqua-pink)" textLength="368" lengthAdjust="spacingAndGlyphs">GLE</text>
    </g>

    <g class="details-frame">
      <path d="M860,52 Q1000,22 1140,52 Q1150,100 1168,120 L1168,490 Q1150,510 1140,546 Q1000,572 860,546 Q850,510 832,490 L832,120 Q850,100 860,52 Z"
            fill="var(--white)" stroke="var(--berry)" stroke-width="12" stroke-linejoin="round"/>
      <path d="M872,68 Q1000,42 1128,68 Q1136,108 1152,126 L1152,484 Q1136,502 1128,530 Q1000,554 872,530 Q864,502 848,484 L848,126 Q864,108 872,68 Z"
            fill="none" stroke="var(--hot-pink)" stroke-width="2"/>
    </g>

    <g class="details">
      <text class="detail-label" x="1000" y="118" font-size="26">WHO</text>
      <text class="detail-value" x="1000" y="160" font-size="34">RINA</text>
      <text class="detail-label" x="1000" y="200" font-size="26">WHAT</text>
      <text class="detail-value" x="1000" y="240" font-size="21">BACHELORETTE PARTY</text>
      <text class="detail-label" x="1000" y="286" font-size="26">WHEN</text>
      <text class="detail-value" x="1000" y="326" font-size="21">7TH OF FEBRUARY 2013</text>
      <text class="detail-label" x="1000" y="372" font-size="26">WHERE</text>
      <text class="detail-value" x="1000" y="408" font-size="17">TOLO BOAT</text>
      <text class="detail-value" x="1000" y="430" font-size="16" textLength="250" lengthAdjust="spacingAndGlyphs">DUBAI CORAL QUAY SAILING CLUB</text>
      <g class="divider" stroke="var(--berry)" stroke-width="2" fill="var(--hot-pink)">
        <line x1="958" y1="448" x2="1042" y2="448"/>
        <circle cx="1000" cy="448" r="4" stroke="none"/>
      </g>
    </g>
  </svg>
</main>
</body>
</html>
```